Business Card

We are looking to re-create our business card. Attached is the company logo. we would like it to be back and front. for example one side with the persons information and the other side with the company logo. Be as creative as you would like but also keep in mind, we are a Health Insurance company and we need to look professional as well.
Industry/Entity Type
Business

```html
<!DOCTYPE html>
<html lang="en">
<head>
<meta charset="UTF-8">
<title>Alderway Health Partners – Business Card</title>
<link rel="stylesheet" href="https://fonts.googleapis.com/css2?family=Source+Sans+3:wght@400;600&display=swap">
<style>
  :root {
    --stage: #8b8a8f;
    --label: #3a1cf2;
    --card-white: #ffffff;
    --brand-blue: #2a8fd4;
    --name-blue: #1866b4;
    --text-grey: #7d7d7d;
    --rule-grey: #8a8a8a;
    --faint-grey: #ececec;
    --frame-deep: #1f6fae;
    --frame-light: #7cc3ea;
  }
  * { box-sizing: border-box; margin: 0; padding: 0; }
  html, body { width: 1200px; height: 900px; overflow: hidden; }
  body {
    background: var(--stage);
    font-family: "Source Sans 3", sans-serif;
    position: relative;
  }
  .card {
    position: absolute;
    top: 257px;
    width: 575px;
    height: 336px;
    overflow: hidden;
  }
  .card--front { left: 10px; }
  .card--back { left: 610px; }

  .card__frame {
    position: absolute;
    inset: 0;
    background: linear-gradient(135deg, var(--frame-deep) 0%, var(--frame-light) 100%);
  }
  .card__face {
    position: absolute;
    left: 7px; top: 10px; right: 8px; bottom: 10px;
    background: var(--card-white);
    border-radius: 42px;
    overflow: hidden;
  }

  .brand {
    display: flex;
    align-items: center;
    gap: 10px;
    color: var(--brand-blue);
    font-weight: 400;
    white-space: nowrap;
  }
  .brand__mark {
    width: 14px; height: 14px;
    background: var(--brand-blue);
  }
  .card--front .brand {
    position: absolute;
    left: 0; right: 0; top: 131px;
    justify-content: center;
    font-size: 30px;
  }
  .url {
    position: absolute;
    left: 0; right: 0; top: 282px;
    text-align: center;
    font-size: 12.5px;
    color: var(--text-grey);
  }

  .card--back .brand {
    position: absolute;
    left: 14px; top: 36px;
    font-size: 25px;
  }
  .backdrop-name {
    position: absolute;
    left: 14px; top: 108px;
    font-size: 100px;
    line-height: 1;
    font-weight: 600;
    color: var(--faint-grey);
    letter-spacing: -1px;
    white-space: nowrap;
  }
  .person {
    position: absolute;
    right: 24px; top: 193px;
    text-align: right;
  }
  .person__name {
    font-size: 23px;
    font-weight: 600;
    color: var(--name-blue);
    line-height: 1.1;
  }
  .person__role {
    font-size: 14px;
    color: var(--text-grey);
    margin-right: 14px;
    line-height: 1.2;
  }
  .divider {
    position: absolute;
    left: 16px; top: 240px;
    width: 405px; height: 1px;
    background: var(--rule-grey);
  }
  .contact {
    position: absolute;
    right: 384px; top: 240px;
    list-style: none;
    font-size: 12.5px;
    color: var(--text-grey);
    line-height: 14px;
    text-align: right;
  }
  .contact li { display: flex; align-items: center; justify-content: flex-end; gap: 6px; }
  .contact svg { width: 11px; height: 11px; flex: none; }

  .side-label {
    position: absolute;
    top: 608px;
    width: 575px;
    text-align: center;
    font-size: 76px;
    font-weight: 600;
    color: var(--label);
  }
  .side-label--front { left: 10px; }
  .side-label--back { left: 572px; }
</style>
</head>
<body>

  <section class="card card--front">
    <div class="card__frame" role="img" aria-label="Soft colour frame around the card"></div>
    <div class="card__face">
      <div class="brand"><span class="brand__mark"></span>Alderway Health Partners</div>
      <p class="url">Your url here</p>
    </div>
  </section>

  <section class="card card--back">
    <div class="card__frame" role="img" aria-label="Soft colour frame around the card"></div>
    <div class="card__face">
      <div class="backdrop-name" aria-hidden="true">Alderway</div>
      <div class="brand"><span class="brand__mark"></span>Alderway Health Partners</div>
      <div class="person">
        <p class="person__name">Your Name</p>
        <p class="person__role">Designation</p>
      </div>
      <div class="divider"></div>
      <ul class="contact">
        <li>Your Email Address here
          <svg viewBox="0 0 12 12" aria-hidden="true"><rect x="0.5" y="2.5" width="11" height="7" fill="#111"/><path d="M0.5 2.5 L6 7 L11.5 2.5" stroke="#fff" stroke-width="1" fill="none"/></svg>
        </li>
        <li>Your Phone Number
          <svg viewBox="0 0 12 12" aria-hidden="true"><rect x="3.5" y="1" width="5" height="10" rx="1" fill="none" stroke="#111" stroke-width="1"/></svg>
        </li>
        <li>Your Address Here
          <svg viewBox="0 0 12 12" aria-hidden="true"><path d="M6 11.5 C3 8 2.5 6.5 2.5 5 A3.5 3.5 0 0 1 9.5 5 C9.5 6.5 9 8 6 11.5 Z" fill="#111"/><circle cx="6" cy="5" r="1.4" fill="#fff"/></svg>
        </li>
      </ul>
    </div>
  </section>

  <h2 class="side-label side-label--front">Front</h2>
  <h2 class="side-label side-label--back">Back</h2>

</body>
</html>
```